A Freight forwarding (transportation/shipping) company requires stationary designs

We need The following:
1. Letterhead
2. Letter Envelope
3. Business Card Design
4. A4 Paper Envelope
5. A4 Paper Folder (One that is 2xA4 foldable size which we can open in half and we can put a paper in between and has a lot for business card)
6. A5 Paper (To be used for notes taking)
a design for a freight forwarding company named KORVELA MIND INTERNATIONAL TRANSPORTATION.
(We are active in Sea Transportation, Truck transportation, and Air Transportation, (printed design in PDF is required with all open source files for editing - lamination accepted)
Playing around with the Logo is accepted,, Korvela Logo.png is the correct logo.
Example of folder, envelopes, and notepad attached
Address of the company is :
No 7, 4th Tarandil Gharbi, Neshat Lar Blvd,
Mashhad, IR
Tel : +98 51 37412958
Fax : +98 51 37490316
Website : www.korvela-example.com
Email : info@korvela-example.com

```html
<!DOCTYPE html>
<html lang="en">
<head>
<meta charset="utf-8">
<title>Korvela Mind – Business Card</title>
<link href="https://fonts.googleapis.com/css2?family=Open+Sans:wght@400;600;700&display=swap" rel="stylesheet">
<style>
  :root {
    --page: #d8d6d3;
    --card: #141416;
    --violet: #4a4fc4;
    --ring: #3a3e92;
    --green: #3f9a3f;
    --text: #e8e8e8;
    --muted: #9a9a9e;
  }
  * { box-sizing: border-box; margin: 0; padding: 0; }
  html, body { width: 1200px; height: 864px; overflow: hidden; }
  body {
    background: var(--page);
    font-family: "Open Sans", Arial, sans-serif;
    position: relative;
  }
  .card {
    position: absolute;
    top: 278px;
    width: 540px;
    height: 309px;
    background: var(--card);
    border-radius: 3px;
    box-shadow: 0 10px 30px rgba(0,0,0,.25);
    overflow: hidden;
  }
  .card--front { left: 40px; }
  .card--back { left: 620px; }

  /* Front */
  .brand-mark {
    position: absolute;
    left: 50%;
    top: 58px;
    transform: translateX(-50%);
    display: flex;
    flex-direction: column;
    align-items: center;
    gap: 14px;
  }
  .brand-mark__dot {
    width: 96px; height: 96px;
    border-radius: 50%;
    background: var(--ring);
  }
  .brand-mark__name {
    color: var(--text);
    font-weight: 600;
    font-size: 17px;
    letter-spacing: 3px;
  }
  .front-web {
    position: absolute;
    left: 0; right: 0;
    top: 238px;
    text-align: center;
    color: var(--muted);
    font-size: 13px;
    letter-spacing: 5px;
  }

  /* Back */
  .person {
    position: absolute;
    left: 30px;
    top: 58px;
  }
  .person__name {
    color: var(--violet);
    font-weight: 700;
    font-size: 17px;
    letter-spacing: .5px;
  }
  .person__role {
    color: var(--green);
    font-size: 14px;
    margin-top: 1px;
  }
  .contacts {
    position: absolute;
    left: 30px;
    top: 112px;
    list-style: none;
  }
  .contacts li {
    display: flex;
    align-items: center;
    gap: 8px;
    color: var(--text);
    font-size: 13.5px;
    line-height: 19px;
  }
  .contacts svg { width: 11px; height: 11px; fill: var(--violet); flex: none; }
  .divider {
    position: absolute;
    left: 30px; right: 30px;
    top: 196px;
    height: 1px;
    background: var(--violet);
  }
  .back-brand {
    position: absolute;
    right: 30px;
    top: 40px;
    display: flex;
    flex-direction: column;
    align-items: center;
  }
  .back-brand__dot {
    width: 86px; height: 86px;
    border-radius: 50%;
    background: var(--ring);
    margin-bottom: 8px;
  }
  .back-brand__name {
    color: var(--text);
    font-size: 15px;
    font-weight: 400;
    letter-spacing: .5px;
  }
  .back-brand__tag {
    color: var(--text);
    font-size: 7.5px;
  }
  .address {
    position: absolute;
    right: 30px;
    top: 208px;
    text-align: right;
    color: var(--text);
    font-size: 14px;
    line-height: 19px;
    font-style: normal;
  }
</style>
</head>
<body>

<section class="card card--front">
  <div class="brand-mark">
    <span class="brand-mark__dot"></span>
    <span class="brand-mark__name">KORVELA MIND</span>
  </div>
  <p class="front-web">www.korvela-example.com</p>
</section>

<section class="card card--back">
  <div class="person">
    <p class="person__name">DARIUS NAVEH</p>
    <p class="person__role">CEO/FOUNDER</p>
  </div>

  <ul class="contacts">
    <li>
      <svg viewBox="0 0 12 12"><path d="M2.5 1l2 2.2-1 1.3c.7 1.5 1.8 2.6 3.2 3.3l1.3-1 2.2 2-1.2 1.9C4.7 10.6 1.4 7.3 1 2.4z"/></svg>
      +98 51 37412958
    </li>
    <li>
      <svg viewBox="0 0 12 12"><rect x="3" y="1" width="6" height="3"/><rect x="1" y="4.5" width="10" height="4.5" rx="1"/><rect x="3" y="8" width="6" height="3"/></svg>
      +98 51 37490316
    </li>
    <li>
      <svg viewBox="0 0 12 12"><path d="M1 2.5h10v7H1z M1.5 3l4.5 3.5L10.5 3" stroke="#141416" stroke-width=".8"/></svg>
      info@korvela-example.com
    </li>
    <li>
      <svg viewBox="0 0 12 12"><circle cx="6" cy="6" r="5"/><path d="M1 6h10M6 1c2 2.5 2 7.5 0 10M6 1c-2 2.5-2 7.5 0 10" stroke="#141416" stroke-width=".7" fill="none"/></svg>
      www.korvela-example.com
    </li>
  </ul>

  <div class="back-brand">
    <span class="back-brand__dot"></span>
    <span class="back-brand__name">KORVELA MIND</span>
    <span class="back-brand__tag">International Transportation</span>
  </div>

  <div class="divider"></div>

  <address class="address">
    No 7, 4th Tarandil<br>
    Gharbi<br>
    Neshat Lar<br>
    Blvd, Mashhad, IR
  </address>
</section>

</body>
</html>
```